Business Card Design

I need a business card for my Heating / Cooling Business. I've been in the business for 28 years. The name of the company is "Tom's Heating and Cooling".
Designers, I've attached an old business card we've used to copy the information.
Take off 15 years of experience
Industry/Entity Type
Business
Contact Information for Business Card
Gene Waltham and Lorna Waltham(740)-795-4758

```html
<!DOCTYPE html>
<html lang="en">
<head>
<meta charset="utf-8">
<title>Tom's Heating &amp; Cooling — Business Card</title>
<link rel="stylesheet" href="https://fonts.googleapis.com/css2?family=Open+Sans:wght@400;600;700&display=swap">
<style>
  :root {
    --teal-deep: #3aaec4;
    --teal-mid: #62c2c9;
    --teal-soft: #9fd6cc;
    --card-white: #ffffff;
    --ink-grey: #8a8a8a;
    --ink-light: #ffffff;
  }
  * { margin: 0; padding: 0; box-sizing: border-box; }
  html, body {
    width: 1200px; height: 702px; overflow: hidden;
    background: var(--card-white);
  }
  .card {
    position: relative; width: 1200px; height: 702px;
    background: var(--card-white);
    font-family: "Open Sans", Arial, sans-serif;
    overflow: hidden;
  }
  .brand-panel { position: absolute; inset: 0; }
  .brand-mark {
    position: absolute; left: 137px; top: 205px;
    width: 182px; height: 182px; border-radius: 50%;
    background: var(--card-white);
  }
  .brand-name {
    position: absolute; left: 27px; width: 400px; top: 402px;
    text-align: center; color: var(--ink-light); font-weight: 600;
    line-height: 1;
  }
  .brand-name .first { display: block; font-size: 54px; letter-spacing: 0.5px; }
  .brand-name .rest { display: block; font-size: 28px; margin-top: 18px; }
  .info {
    position: absolute; left: 600px; width: 560px;
    text-align: center; color: var(--ink-grey); text-transform: uppercase;
  }
  .services-title { top: 96px; font-size: 26px; font-weight: 700; }
  .services-list { top: 166px; list-style: none; font-size: 21px; font-weight: 600; line-height: 28px; }
  .contact { top: 390px; }
  .contact-name {
    display: inline-flex; align-items: center; gap: 10px;
    font-size: 25px; font-weight: 400;
  }
  .contact-name svg { width: 32px; height: 32px; fill: var(--ink-grey); }
  .contact-phone { font-size: 20px; font-weight: 600; margin-top: 2px; padding-left: 10px; }
  .address { top: 552px; font-size: 21px; font-weight: 600; line-height: 29px; }
</style>
</head>
<body>
<main class="card">
  <div class="brand-panel">
    <svg width="1200" height="702" viewBox="0 0 1200 702" role="img" aria-label="Teal honeycomb pattern background">
      <defs>
        <linearGradient id="tealFade" x1="0" y1="0" x2="0.6" y2="1">
          <stop offset="0" stop-color="var(--teal-deep)"/>
          <stop offset="0.55" stop-color="var(--teal-mid)"/>
          <stop offset="1" stop-color="var(--teal-soft)"/>
        </linearGradient>
      </defs>
      <polygon points="0,0 636,0 448,352 608,702 0,702" fill="url(#tealFade)"/>
    </svg>
    <div class="brand-mark"></div>
    <h1 class="brand-name">
      <span class="first">TOM'S</span>
      <span class="rest">HEATING &amp; COOLING</span>
    </h1>
  </div>

  <h2 class="info services-title">Installation &amp; Service</h2>
  <ul class="info services-list">
    <li>Small Appliance Repair</li>
    <li>Plumbing</li>
    <li>Refrigiration</li>
    <li>Car Airconditioning</li>
    <li>Professional Mobile Home Installation</li>
  </ul>

  <div class="info contact">
    <div class="contact-name">
      <svg viewBox="0 0 24 24" aria-hidden="true"><path d="M6.6 10.8a15.1 15.1 0 0 0 6.6 6.6l2.2-2.2a1 1 0 0 1 1-.25 11.4 11.4 0 0 0 3.6.57 1 1 0 0 1 1 1V20a1 1 0 0 1-1 1A17 17 0 0 1 3 4a1 1 0 0 1 1-1h3.5a1 1 0 0 1 1 1c0 1.25.2 2.45.57 3.57a1 1 0 0 1-.25 1z"/></svg>
      <span>Gene Waltham</span>
    </div>
    <div class="contact-phone">(612)-438-2091</div>
  </div>

  <address class="info address" style="font-style:normal">
    2187 Maple Ridge Road<br>
    Cedar Falls, Ohio 43119
  </address>
</main>
</body>
</html>
```